Marla Hensley Book Cover

- 6x9 book cover.
- Book title: Unlearning the busy calendar trap - a widow's road from ruin to fortune
- Back cover will show the 3 testimonials along with their pictures ( we only have two atm, so please just leave a space for a 3rd ). Back cover will also include "about the author"
- Front cover to feature author's picture and background should have nature view ( outside window )
- Author's text: ( The language about me )
This is one woman’s story about her journey from the depths of despair to happiness and financial success. She stopped chasing the Busy-Calendar Trap. Marla shares the steps she then took to change her life.
Listed in Halvern Merit Registry, Prairie Ledger Honorees and more Marla Hensley provides hands on, real life advice to help you make remarkable changes in your life.

```html
<!DOCTYPE html>
<html lang="en">
<head>
<meta charset="utf-8">
<title>Marla Hensley Book Cover</title>
<link rel="stylesheet" href="https://fonts.googleapis.com/css2?family=Anton&family=Delius&family=Tinos:wght@400;700&display=swap">
<style>
  :root {
    --page: #ffffff;
    --ink: #000000;
    --paper: #ffffff;
    --frame-grey: #b3b3b3;
    --slot-grey: #7a7a7a;
    --portrait-light: #f4efe9;
    --portrait-mid: #d9c2b0;
    --portrait-hair: #e3e0da;
    --headshot-warm: #8a6a55;
    --headshot-dark: #3a2a22;
  }
  * { margin: 0; padding: 0; box-sizing: border-box; }
  html, body { width: 1200px; height: 1200px; overflow: hidden; background: var(--page); }

  .cover-spread {
    position: absolute;
    left: 145px; top: 272px;
    width: 911px; height: 656px;
    display: flex;
    box-shadow: 6px 10px 14px rgba(0,0,0,0.35);
  }

  /* Back cover */
  .back-cover {
    position: relative;
    width: 438px; height: 100%;
    background: var(--ink);
    color: var(--paper);
    font-family: "Tinos", "Times New Roman", serif;
  }
  .about-heading {
    position: absolute; left: 42px; top: 86px;
    width: 348px;
    font-size: 10.5px; font-weight: 700;
    border-bottom: 1px solid var(--paper);
    line-height: 12px;
  }
  .about-text {
    position: absolute; left: 42px; top: 108px;
    width: 366px;
    font-size: 11.2px; line-height: 14px;
  }
  .testimonial-photo {
    position: absolute; left: 42px;
    width: 114px; height: 114px;
  }
  .testimonial-photo svg { display: block; }
  .testimonial-quote {
    position: absolute;
    width: 250px;
    font-size: 8.6px; line-height: 11.6px;
  }
  .testimonial-quote strong { font-weight: 700; }

  /* Spine */
  .spine {
    position: relative;
    width: 35px; height: 100%;
    background: var(--paper);
  }
  .spine-title {
    position: absolute; left: 32px; top: 166px;
    transform-origin: 0 0;
    transform: rotate(90deg);
    white-space: nowrap;
    font-family: "Anton", "Impact", sans-serif;
    font-size: 19px; letter-spacing: 0.2px;
    color: var(--ink);
  }

  /* Front cover */
  .front-cover {
    position: relative;
    width: 438px; height: 100%;
    background: var(--ink);
    overflow: hidden;
  }
  .front-cover .splash { position: absolute; inset: 0; }
  .front-title {
    position: absolute; left: 0; top: 64px; width: 100%;
    text-align: center;
    font-family: "Anton", "Impact", sans-serif;
    font-size: 36px; line-height: 46px;
    color: var(--paper);
    text-shadow: 2px 2px 2px rgba(120,120,120,0.8);
  }
  .front-subtitle {
    position: absolute; left: 0; top: 168px; width: 100%;
    text-align: center;
    font-family: "Delius", "Comic Sans MS", cursive;
    font-size: 13.5px;
    color: var(--paper);
  }
  .author-portrait {
    position: absolute; left: 62px; top: 228px;
    width: 310px; height: 428px;
  }
  .author-name {
    position: absolute; left: 0; top: 596px; width: 100%;
    text-align: center;
    font-family: "Tinos", "Times New Roman", serif;
    font-weight: 700; font-size: 19px; letter-spacing: 1.5px;
    color: var(--ink);
  }
</style>
</head>
<body>
  <div class="cover-spread">

    <section class="back-cover">
      <h2 class="about-heading">About the Author</h2>
      <p class="about-text">This is one woman’s story about her journey from the depths of despair to happiness and financial success. She stopped chasing the Busy-Calendar Trap. Marla shares the steps she then took to change her life.<br>Listed in Halvern Merit Registry, Prairie Ledger Honorees and more Marla Hensley provides hands on, real life advice to help you make remarkable changes in your life.</p>

      <div class="testimonial-photo" style="top:248px">
        <svg width="114" height="114" viewBox="0 0 114 114">
          <polygon points="0,14 109,0 99,112 0,112" fill="var(--frame-grey)"/>
          <rect x="0.5" y="13.5" width="98" height="98" fill="var(--headshot-warm)" stroke="var(--paper)" stroke-width="1" role="img" aria-label="Portrait of testimonial author Rhea Calloway"/>
        </svg>
      </div>
      <p class="testimonial-quote" style="left:156px; top:286px">“As a clarity, leadership &amp;communication strategist, I found Marla’s advice to be down to earth, providing a no-nonsense foundation to begin making the life changes women want.”<br><strong>Rhea Calloway,</strong> Author of the Quiet Ladder</p>

      <div class="testimonial-photo" style="top:364px">
        <svg width="114" height="114" viewBox="0 0 114 114">
          <polygon points="0,14 109,0 99,112 0,112" fill="var(--frame-grey)"/>
          <rect x="0.5" y="13.5" width="98" height="98" fill="var(--headshot-dark)" stroke="var(--paper)" stroke-width="1" role="img" aria-label="Portrait of testimonial author Tamsin Orvell"/>
        </svg>
      </div>
      <p class="testimonial-quote" style="left:153px; top:386px">As our world gets increasingly more stressful, the complexities of trying to develop true balance in our lives, work, and relationships adds more stress. In her book, Marla Hensley offers sound advice on how to create and maintain a healthy lifestyle.&nbsp; This book is a must have!<br><strong>Tamsin Orvell,</strong> Harbor Tower Survivor, Lakeside Review Best-Selling Author and Founder of The Open Table Project</p>

      <div class="testimonial-photo" style="top:484px">
        <svg width="114" height="114" viewBox="0 0 114 114">
          <polygon points="0,14 109,0 99,112 0,112" fill="var(--frame-grey)"/>
          <rect x="0.5" y="13.5" width="98" height="98" fill="var(--slot-grey)" stroke="var(--paper)" stroke-width="1" role="img" aria-label="Reserved space for third testimonial portrait"/>
        </svg>
      </div>
    </section>

    <div class="spine">
      <span class="spine-title">Unlearning the busy calendar trap</span>
    </div>

    <section class="front-cover">
      <svg class="splash" width="438" height="656" viewBox="0 0 438 656" aria-hidden="true">
        <path d="M0,246 C30,232 60,262 96,250 C130,238 150,222 178,226 C210,230 240,212 276,222 C320,234 350,208 380,216 C404,222 420,236 438,232 L438,656 L0,656 Z" fill="var(--paper)"/>
        <path d="M438,40 L438,58 L430,52 Z" fill="var(--paper)"/>
      </svg>
      <h1 class="front-title">Unlearning the busy<br>calendar trap</h1>
      <p class="front-subtitle">a widow's road from ruin to fortune</p>
      <svg class="author-portrait" viewBox="0 0 310 428" role="img" aria-label="Portrait of author Marla Hensley by a window with a nature view">
        <defs>
          <radialGradient id="portraitTone" cx="50%" cy="48%" r="55%">
            <stop offset="0%" stop-color="var(--portrait-mid)"/>
            <stop offset="45%" stop-color="var(--portrait-hair)"/>
            <stop offset="80%" stop-color="var(--portrait-light)"/>
            <stop offset="100%" stop-color="var(--paper)" stop-opacity="0"/>
          </radialGradient>
        </defs>
        <rect width="310" height="428" fill="url(#portraitTone)"/>
      </svg>
      <p class="author-name">Marla Hensley</p>
    </section>

  </div>
</body>
</html>
```